New customer flyer

Looking for a flyer that can be written on as a field estimate for door to door sales
Ideally have some nice on the front with the back as a estimate form
Doorknob hanger size

Target Market(s)

Home owners buying core aeration service

Industry/Entity Type

Lawn Care

Requirements
Must have
• Logo
• First name
• Last name
• Cell
• Email
• Address
• Sq ft
Nice to have
• Benefits of core aeration

```html
<!DOCTYPE html>
<html lang="en">
<head>
<meta charset="utf-8">
<title>TurfVent – Door Hanger Estimate</title>
<link rel="stylesheet" href="https://fonts.googleapis.com/css2?family=Arimo:wght@400;700&family=Bebas+Neue&display=swap">
<style>
  :root {
    --backdrop: #111111;
    --sky-blue: #2f74f0;
    --deep-blue: #3377e8;
    --leaf-green: #4c8f38;
    --grass-green: #4aa84a;
    --paper: #ffffff;
    --ink: #333333;
    --ink-dark: #111111;
    --rule: #9a9a9a;
  }
  * { margin: 0; padding: 0; box-sizing: border-box; }
  html, body {
    width: 1200px; height: 1200px; overflow: hidden;
    background: var(--backdrop);
  }
  .stage { position: relative; width: 1200px; height: 1200px; }
  .hanger {
    position: absolute; top: 97px;
    width: 383px; height: 990px;
    display: block;
  }
  .hanger--front { left: 144px; }
  .hanger--back { left: 651px; }
  .brand-name { font-family: 'Arimo', Arial, sans-serif; font-weight: 700; fill: var(--leaf-green); }
  .brand-line { font-family: 'Arimo', Arial, sans-serif; font-size: 17px; fill: var(--ink-dark); }
  .headline-kicker { font-family: 'Arimo', Arial, sans-serif; font-size: 34px; fill: var(--paper); }
  .headline { font-family: 'Bebas Neue', 'Oswald', sans-serif; fill: var(--paper); }
  .benefit-intro { font-family: 'Arimo', Arial, sans-serif; font-size: 40px; fill: var(--ink); }
  .benefit-title { font-family: 'Bebas Neue', 'Oswald', sans-serif; font-size: 88px; }
  .benefit-title .word-core { fill: var(--sky-blue); }
  .benefit-title .word-aeration { fill: var(--leaf-green); }
  .benefit-copy { font-family: 'Arimo', Arial, sans-serif; font-size: 23px; fill: var(--ink); }
  .field-label { font-family: 'Arimo', Arial, sans-serif; font-weight: 700; font-size: 24px; fill: var(--paper); }
  .field-box { fill: var(--paper); stroke: #1b2a4a; stroke-width: 1.5; }
</style>
</head>
<body>
<main class="stage">

  <!-- Front side -->
  <svg class="hanger hanger--front" viewBox="0 0 616 1594" xmlns="http://www.w3.org/2000/svg">
    <defs>
      <linearGradient id="front-scene" x1="0" y1="0" x2="0" y2="1">
        <stop offset="0" stop-color="#2f74f0"/>
        <stop offset="0.3" stop-color="#3f8fe0"/>
        <stop offset="0.5" stop-color="#5a9a4a"/>
        <stop offset="0.75" stop-color="#4f9a38"/>
        <stop offset="1" stop-color="#6cc04a"/>
      </linearGradient>
      <linearGradient id="front-wave" x1="0" y1="0" x2="1" y2="0">
        <stop offset="0.55" stop-color="#2f74f0"/>
        <stop offset="1" stop-color="#4aa84a"/>
      </linearGradient>
    </defs>
    <rect width="616" height="1594" fill="var(--paper)"/>
    <path class="panel-sky" d="M0,255 C150,320 450,335 616,258 L616,1260 L0,1260 Z" fill="var(--sky-blue)"/>
    <g class="panel-photo" role="img" aria-label="Photo of a man riding a red zero-turn mower across a green lawn in front of a white house with trees">
      <rect x="0" y="470" width="616" height="790" fill="url(#front-scene)"/>
    </g>
    <path class="panel-top-band" d="M0,250 C200,330 450,300 616,125 L616,262 C420,340 180,345 0,258 Z" fill="var(--leaf-green)"/>
    <path class="panel-lower-wave" d="M0,1125 Q300,1040 616,1240 L616,1594 L0,1594 Z" fill="url(#front-wave)"/>
    <path class="panel-lower-paper" d="M0,1258 Q300,1070 616,1240 L616,1594 L0,1594 Z" fill="var(--paper)"/>

    <g class="brand">
      <text class="brand-name" x="300" y="160" font-size="70" text-anchor="middle">TurfVent</text>
      <text class="brand-line" x="300" y="190" text-anchor="middle">Core Aeration Specialists</text>
    </g>

    <text class="headline-kicker" x="302" y="385" text-anchor="middle">Helping your Lawns</text>
    <text class="headline" x="304" y="515" font-size="162" text-anchor="middle" textLength="394" lengthAdjust="spacingAndGlyphs">BREATHE</text>
    <text class="headline" x="304" y="622" font-size="130" text-anchor="middle">AGAIN</text>

    <text class="benefit-intro" x="308" y="1252" text-anchor="middle">Benefits of</text>
    <text class="benefit-title" x="308" y="1325" text-anchor="middle"><tspan class="word-core">CORE</tspan> <tspan class="word-aeration">AERATION</tspan></text>

    <text class="benefit-copy" text-anchor="middle">
      <tspan x="300" y="1378">Helps the roots grow deeply and produce a</tspan>
      <tspan x="300" y="1403">stronger, more vigorous lawn.</tspan>
    </text>
    <line x1="18" y1="1420" x2="588" y2="1420" stroke="var(--rule)" stroke-width="1.5"/>
    <text class="benefit-copy" text-anchor="middle">
      <tspan x="300" y="1451">The main reason for aerating is to alleviate</tspan>
      <tspan x="300" y="1475">soil compaction.</tspan>
    </text>
    <text class="benefit-copy" text-anchor="middle">
      <tspan x="300" y="1523">Helps the roots grow deeply and produce a</tspan>
      <tspan x="300" y="1548">stronger, more vigorous lawn.</tspan>
    </text>
  </svg>

  <!-- Back side: estimate form -->
  <svg class="hanger hanger--back" viewBox="0 0 616 1594" xmlns="http://www.w3.org/2000/svg">
    <defs>
      <linearGradient id="back-top" x1="0" y1="0" x2="0" y2="1">
        <stop offset="0" stop-color="#48ad68"/>
        <stop offset="1" stop-color="#52bd3a"/>
      </linearGradient>
      <linearGradient id="back-photo" x1="0" y1="0" x2="0" y2="1">
        <stop offset="0" stop-color="#c9d4e0"/>
        <stop offset="0.45" stop-color="#6a8fc4"/>
        <stop offset="1" stop-color="#c23a35"/>
      </linearGradient>
    </defs>
    <rect width="616" height="1594" fill="var(--paper)"/>
    <path class="panel-blue" d="M0,258 C150,320 450,335 616,258 L616,1500 L0,1500 Z" fill="var(--deep-blue)"/>
    <path class="panel-top-band" d="M0,0 H616 V125 C450,300 150,310 0,250 Z" fill="url(#back-top)"/>

    <text class="headline-kicker" x="17" y="85">Helping your Lawns</text>
    <text class="headline" x="14" y="182" font-size="112" textLength="463" lengthAdjust="spacingAndGlyphs">BREATHE AGAIN</text>

    <g class="estimate-form">
      <text class="field-label" x="63" y="408">First name</text>
      <rect class="field-box" x="61" y="424" width="492" height="63" rx="5"/>
      <text class="field-label" x="63" y="529">Last name</text>
      <rect class="field-box" x="61" y="541" width="492" height="63" rx="5"/>
      <text class="field-label" x="63" y="650">Cell</text>
      <rect class="field-box" x="61" y="661" width="492" height="63" rx="5"/>
      <text class="field-label" x="63" y="770">Email</text>
      <rect class="field-box" x="61" y="782" width="492" height="63" rx="5"/>
      <text class="field-label" x="63" y="891">Address</text>
      <rect class="field-box" x="61" y="903" width="492" height="63" rx="5"/>
      <text class="field-label" x="63" y="1012">Area (in sq ft)</text>
      <rect class="field-box" x="61" y="1024" width="492" height="63" rx="5"/>
    </g>

    <path class="panel-lower-green" d="M0,1365 Q250,1290 616,1440 L616,1594 L0,1594 Z" fill="var(--grass-green)"/>
    <g class="panel-photo" role="img" aria-label="Cut-out photo of a man driving a red zero-turn mower">
      <rect x="128" y="1098" width="350" height="310" rx="30" fill="url(#back-photo)"/>
    </g>
    <path class="panel-lower-paper" d="M0,1490 Q320,1250 616,1440 L616,1594 L0,1594 Z" fill="var(--paper)"/>

    <g class="brand">
      <text class="brand-name" x="308" y="1530" font-size="70" text-anchor="middle">TurfVent</text>
      <text class="brand-line" x="308" y="1560" text-anchor="middle">Core Aeration Specialists</text>
    </g>
  </svg>

</main>
</body>
</html>
```